Healthy Supplement featuring Moringa products

Need 3 business card options for our reps to order from Cardloom. Our reps will be ordering from Cardloom once we upload them. Attached is our current designs to show what info needs to be on the cards. Our website is www.tkvitality.com
The business cards will be a template for our reps to order from. Most of our reps are Asian & Hispanic. Please look at our website so you can see who we are to get the look and feel what we need.
Target Market(s)
Adults 30 on up. Health oriented people.
Industry/Entity Type
Health And Wellness
Contact Information for Business Card
Name
Title
Phone
Logo
www.tkvitality.com/my/username
Font styles to use
Requirements
Must have
- Please match our website look and colors. A moringa leaf is nice, but am open to something different.
Nice to have
- Healthy looking and warm, not super cold or too modern.
Should not have
- No harsh colors please.

```html
<!DOCTYPE html>
<html lang="en">
<head>
<meta charset="UTF-8">
<title>TK Vitality – Representative Business Card</title>
<link href="https://fonts.googleapis.com/css2?family=Arimo:wght@400;700&display=swap" rel="stylesheet">
<style>
  :root {
    --leaf-green: #6aaa44;
    --bright-green: #8cc63f;
    --deep-green: #5a9e35;
    --accent-orange: #f07022;
    --ink: #1f1f1f;
    --paper: #ffffff;
    --backdrop: #d9dbdd;
  }
  * { margin: 0; padding: 0; box-sizing: border-box; }
  html, body { width: 1200px; height: 800px; overflow: hidden; }
  body {
    background: var(--backdrop);
    font-family: "Arimo", Arial, sans-serif;
    position: relative;
  }
  .card {
    position: absolute;
    width: 540px;
    height: 309px;
    overflow: hidden;
    box-shadow: 0 6px 18px rgba(0,0,0,0.18);
  }
  /* Front: solid green with brand name */
  .card--front {
    left: 610px; top: 150px;
    background: var(--leaf-green);
    display: flex; align-items: center; justify-content: center;
  }
  .brand {
    display: flex; align-items: center; gap: 14px;
    font-weight: 700;
    letter-spacing: 1px;
  }
  .brand__dot { border-radius: 50%; flex: none; }
  .card--front .brand { font-size: 46px; color: var(--paper); }
  .card--front .brand__dot { width: 34px; height: 34px; background: var(--paper); }

  /* Back: contact details */
  .card--back {
    left: 60px; top: 330px;
    background: var(--paper);
  }
  .card--back .brand {
    position: absolute; left: 46px; top: 42px;
    font-size: 34px; color: var(--leaf-green);
  }
  .card--back .brand__dot { width: 26px; height: 26px; background: var(--bright-green); }

  .contact-tab {
    position: absolute; left: 0; top: 132px;
    width: 34px; height: 78px;
    background: var(--accent-orange);
    border-radius: 0 8px 8px 0;
    display: flex; flex-direction: column; align-items: center; justify-content: space-evenly;
  }
  .contact-tab svg { width: 14px; height: 14px; }
  .contact-list {
    position: absolute; left: 48px; top: 138px;
    list-style: none;
    font-size: 17px; line-height: 23px; color: var(--ink);
  }
  .rep {
    position: absolute; left: 330px; top: 118px;
  }
  .rep__name { font-size: 22px; font-weight: 700; color: var(--bright-green); }
  .rep__title { font-size: 16px; color: var(--accent-orange); margin-top: 2px; }

  .leaf-spray {
    position: absolute; right: 0; bottom: 0;
    width: 290px; height: 130px;
    border-radius: 120px 0 0 0;
    background: linear-gradient(160deg, var(--bright-green), var(--deep-green));
  }
</style>
</head>
<body>

  <section class="card card--front">
    <div class="brand"><span class="brand__dot"></span>TK Vitality</div>
  </section>

  <section class="card card--back">
    <div class="brand"><span class="brand__dot"></span>TK Vitality</div>

    <div class="contact-tab">
      <svg viewBox="0 0 24 24" fill="#fff"><path d="M6.6 10.8a15.1 15.1 0 0 0 6.6 6.6l2.2-2.2c.3-.3.7-.4 1-.2 1.1.4 2.3.6 3.6.6.6 0 1 .4 1 1V20c0 .6-.4 1-1 1A17 17 0 0 1 3 4c0-.6.4-1 1-1h3.5c.6 0 1 .4 1 1 0 1.3.2 2.5.6 3.6.1.3 0 .7-.2 1z"/></svg>
      <svg viewBox="0 0 24 24" fill="none" stroke="#fff" stroke-width="2"><rect x="3" y="5" width="18" height="14" rx="1"/><path d="M3 6l9 7 9-7"/></svg>
      <svg viewBox="0 0 24 24" fill="none" stroke="#fff" stroke-width="2"><circle cx="12" cy="12" r="9"/><path d="M3 12h18M12 3c3 3 3 15 0 18M12 3c-3 3-3 15 0 18"/></svg>
    </div>

    <ul class="contact-list">
      <li>(123) 456-7890</li>
      <li>daniel@tkvitality.com</li>
      <li>www.tkvitality.com/my/username</li>
    </ul>

    <div class="rep">
      <p class="rep__name">Daniel Reyes</p>
      <p class="rep__title">Representative</p>
    </div>

    <div class="leaf-spray" role="img" aria-label="Illustration of a moringa branch with rounded green leaves"></div>
  </section>

</body>
</html>
```